Billboard for a Contractor in Minnesota

Creating our first billboard that will be displayed on a freeway. Will be used on a digital Flick Signboard. Sign should be a 846 x 234 design. Our website is tamber-paving.com Looking for something specific to "Look us up" or "Call" for your free concrete & asphalt estimate. Needs both web addresses (tamber-paving.com and tamber-masonry.com. Needs our phone number, logo. Our slogan is Serving All Your Asphalt & Concrete Needs. It's also our 25 Anniversary.

Target Market(s)

Residential Homeowners in the Twin Cities

Colors
abd036

Requirements
Must have
• Logo, Phone Number, Our Services, Web Addresses (both) Our services are all on our website. (Asphalt Driveway, Concrete Driveway, Concrete Apron, Concrete Sidewalk, Concrete Patio. Colors should be same as website. Black, White, Gray and the Neon Green color.

```html
<!DOCTYPE html>
<html lang="en">
<head>
<meta charset="utf-8">
<title>Tamber Paving &amp; Masonry – Billboard</title>
<link rel="stylesheet" href="https://fonts.googleapis.com/css2?family=Montserrat:wght@500;600;800&family=Oswald:wght@600;700&display=swap">
<style>
  :root {
    --neon-green: #53cf47;
    --charcoal: #333333;
    --white: #ffffff;
    --ink: #111111;
    --stage: #4b4b4b;
    --badge-ring: #d9d9d9;
    --badge-core: #2f7b5e;
    --badge-ribbon: #8a8a8a;
  }
  html, body {
    margin: 0;
    width: 1200px;
    height: 960px;
    overflow: hidden;
    background: var(--stage);
  }
  .billboard {
    position: absolute;
    left: 40px;
    top: 316px;
    width: 1120px;
    height: 327px;
    box-shadow: 0 18px 30px rgba(0,0,0,.35);
  }
  .brand-name { font-family: "Montserrat", sans-serif; font-weight: 800; fill: var(--ink); }
  .slogan-lead { font-family: "Montserrat", sans-serif; font-weight: 800; fill: var(--white); font-size: 38px; }
  .slogan-main { font-family: "Oswald", sans-serif; font-weight: 700; fill: var(--white); font-size: 66px; }
  .service { font-family: "Montserrat", sans-serif; font-weight: 500; fill: var(--ink); font-size: 23px; }
  .tick { fill: none; stroke: var(--neon-green); stroke-width: 2.5; }
  .cta { font-family: "Montserrat", sans-serif; font-weight: 500; fill: var(--white); font-size: 26px; }
  .cta-free { font-family: "Oswald", sans-serif; font-weight: 700; font-size: 40px; }
  .web { font-family: "Montserrat", sans-serif; font-weight: 600; fill: var(--white); font-size: 31px; }
  .globe { fill: none; stroke: var(--neon-green); stroke-width: 2.4; }
  .phone { font-family: "Oswald", sans-serif; font-weight: 700; fill: var(--neon-green); font-size: 50px; }
</style>
</head>
<body>
<svg class="billboard" viewBox="0 0 1345 393" xmlns="http://www.w3.org/2000/svg" role="img" aria-label="Tamber Paving and Masonry billboard">
  <!-- base panels -->
  <rect class="panel-white" x="0" y="0" width="1345" height="393" fill="var(--white)"/>
  <polygon class="slogan-band" points="380,0 1345,0 1345,158 445,158" fill="var(--neon-green)"/>
  <polygon class="accent-stripe" points="383,28 462,315 432,315 383,92" fill="var(--charcoal)"/>
  <polygon class="cta-band" points="488,250 1345,250 1330,315 506,315" fill="var(--neon-green)"/>
  <rect class="contact-band" x="0" y="315" width="1345" height="78" fill="var(--charcoal)"/>
  <polygon class="phone-panel" points="785,315 1338,315 1325,393 820,393" fill="var(--white)"/>

  <!-- brand name -->
  <g class="brand">
    <text class="brand-name" x="212" y="165" font-size="62" text-anchor="middle" letter-spacing="4">TAMBER</text>
    <text class="brand-name" x="212" y="210" font-size="24" text-anchor="middle" letter-spacing="1">PAVING &amp; MASONRY</text>
  </g>

  <!-- anniversary badge -->
  <g class="anniversary-badge" role="img" aria-label="25th anniversary seal">
    <circle cx="1229" cy="60" r="97" fill="var(--white)"/>
    <circle cx="1229" cy="60" r="86" fill="var(--badge-ring)"/>
    <circle cx="1229" cy="60" r="64" fill="var(--badge-core)"/>
    <rect x="1172" y="88" width="114" height="26" fill="var(--badge-ribbon)"/>
  </g>

  <!-- slogan -->
  <text class="slogan-lead" x="460" y="70" textLength="390" lengthAdjust="spacingAndGlyphs">SERVING ALL YOUR</text>
  <text class="slogan-main" x="460" y="132" textLength="654" lengthAdjust="spacingAndGlyphs">ASPHALT &amp; CONCRETE NEEDS</text>

  <!-- services -->
  <g class="services">
    <path class="tick" d="M507,183 l6,7 l11,-14"/>
    <text class="service" x="528" y="195" textLength="218" lengthAdjust="spacingAndGlyphs">ASPHALT DRIVEWAY</text>
    <path class="tick" d="M785,183 l6,7 l11,-14"/>
    <text class="service" x="807" y="195" textLength="241" lengthAdjust="spacingAndGlyphs">CONCRETE DRIVEWAY</text>
    <path class="tick" d="M1064,183 l6,7 l11,-14"/>
    <text class="service" x="1085" y="195" textLength="206" lengthAdjust="spacingAndGlyphs">CONCRETE APRON</text>
    <path class="tick" d="M507,219 l6,7 l11,-14"/>
    <text class="service" x="527" y="231" textLength="241" lengthAdjust="spacingAndGlyphs">CONCRETE SIDEWALK</text>
    <path class="tick" d="M785,219 l6,7 l11,-14"/>
    <text class="service" x="807" y="231" textLength="190" lengthAdjust="spacingAndGlyphs">CONCRETE PATIO</text>
  </g>

  <!-- call to action -->
  <text class="cta" x="552" y="297" textLength="746" lengthAdjust="spacingAndGlyphs">CALL FOR YOUR <tspan class="cta-free">FREE</tspan> CONCRETE &amp; ASPHALT ESTIMATE</text>

  <!-- web addresses -->
  <g class="web-addresses">
    <g class="globe" transform="translate(57,356)">
      <circle r="13"/><ellipse rx="6" ry="13"/><line x1="-13" y1="0" x2="13" y2="0"/>
    </g>
    <text class="web" x="85" y="367" textLength="290" lengthAdjust="spacingAndGlyphs">tamber-paving.com</text>
    <g class="globe" transform="translate(425,356)">
      <circle r="13"/><ellipse rx="6" ry="13"/><line x1="-13" y1="0" x2="13" y2="0"/>
    </g>
    <text class="web" x="455" y="367" textLength="309" lengthAdjust="spacingAndGlyphs">tamber-masonry.com</text>
  </g>

  <!-- phone -->
  <text class="phone" x="827" y="373" textLength="470" lengthAdjust="spacingAndGlyphs">CALL US: 612-555-0187</text>
</svg>
</body>
</html>
```